Contractor Business Card Design

Looking to have a card made that has a bold description of (KITCHENS, BASEMENTS, BATHROOMS)

Definition and layers a plus

Contact info is;

Mark T. Ellery
Pinecrest, MN 55990
Cell: 612-555-0147
website: www.cobaltfinishworks.example
Email: cobaltfinishworksmn@mailbox.example

colors: red, black, gray, white

Contact Information for Business Card

Contact info is;

Mark T. Ellery
Pinecrest, MN 55990
Cell: 612-555-0147

Colors
ec1f27

Requirements
Must have
• Looking for layers and definition
Nice to have
• Cards are planned to be printed on plastic cards

```html
<!DOCTYPE html>
<html lang="en">
<head>
<meta charset="utf-8">
<title>Cobalt Finish Works – Business Card</title>
<link rel="stylesheet" href="https://fonts.googleapis.com/css2?family=Montserrat:wght@400;500;700&family=Arimo:wght@400&family=Playfair+Display:ital,wght@1,500&display=swap">
<style>
  :root {
    --page: #1f1f21;
    --frost-light: #c9c9cb;
    --frost-dark: #8f8f92;
    --ink: #111113;
    --charcoal: #2a2a2c;
    --brand-red: #ec1f27;
    --white: #ffffff;
    --panel: #f2f2f2;
    --body-text: #333335;
  }
  * { margin: 0; padding: 0; box-sizing: border-box; }
  html, body {
    width: 1200px; height: 800px; overflow: hidden;
    background: var(--page);
    font-family: "Montserrat", sans-serif;
  }
  .card {
    position: absolute;
    left: 290px;
    width: 620px; height: 354px;
    border-radius: 16px;
    overflow: hidden;
    background: linear-gradient(160deg, var(--frost-light) 0%, var(--frost-dark) 100%);
    box-shadow: 0 10px 30px rgba(0,0,0,.45);
  }
  .card--front { top: 30px; }
  .card--back { top: 416px; }

  /* front */
  .front-shapes { position: absolute; inset: 0; width: 100%; height: 100%; }
  .brand {
    position: absolute; left: 70px; top: 48px;
    display: flex; flex-direction: column; align-items: center; gap: 14px;
  }
  .brand__circle {
    width: 88px; height: 88px; border-radius: 50%;
    border: 5px solid var(--brand-red);
  }
  .brand__name {
    font-weight: 700; font-size: 27px; letter-spacing: 1px;
    color: var(--charcoal); text-transform: uppercase; white-space: nowrap;
  }
  .holder {
    position: absolute; left: 40px; top: 270px; color: var(--white);
  }
  .holder__name { font-weight: 700; font-size: 21px; letter-spacing: .5px; text-transform: uppercase; }
  .holder__city { font-weight: 400; font-size: 14px; margin-top: 2px; }
  .contacts {
    position: absolute; left: 318px; top: 282px;
    list-style: none; color: var(--white);
    font-size: 12px; line-height: 20px;
  }
  .contacts li { display: flex; align-items: center; gap: 8px; white-space: nowrap; }
  .contacts svg { width: 13px; height: 13px; flex: none; }

  /* back */
  .back-frame {
    position: absolute; inset: 22px;
    background: var(--ink); padding: 10px;
  }
  .back-panel {
    width: 100%; height: 100%;
    background: var(--panel);
    display: grid; grid-template-columns: repeat(3, 1fr);
    gap: 14px; padding: 16px 16px;
  }
  .service { display: flex; flex-direction: column; align-items: center; text-align: center; }
  .service__photo { width: 100%; height: 118px; }
  .service__photo--basement { background: linear-gradient(135deg, #6b4a2c, #c79a5e 55%, #3d2b20); }
  .service__photo--kitchen { background: linear-gradient(135deg, #d9dde0, #9aa3a8 50%, #b56a3a); }
  .service__photo--install { background: linear-gradient(135deg, #7d746a, #4a4440 55%, #2d3e7a); }
  .service__title {
    font-family: "Playfair Display", serif; font-style: italic; font-weight: 500;
    font-size: 15px; color: var(--ink); margin: 8px 0 4px;
  }
  .service__text {
    font-family: "Arimo", sans-serif; font-size: 9.5px; line-height: 1.3;
    color: var(--body-text);
  }
</style>
</head>
<body>

<section class="card card--front" aria-label="Business card front">
  <svg class="front-shapes" viewBox="0 0 620 354" preserveAspectRatio="none" aria-hidden="true">
    <path d="M0,252 C180,238 420,266 620,300 L620,354 L0,354 Z" fill="var(--ink)"/>
    <path d="M0,206 C200,212 430,256 606,300 C420,268 200,246 0,246 Z" fill="var(--brand-red)"/>
  </svg>

  <div class="brand">
    <span class="brand__circle"></span>
    <span class="brand__name">Cobalt Finish Works</span>
  </div>

  <div class="holder">
    <p class="holder__name">Mark T. Ellery</p>
    <p class="holder__city">Pinecrest, MN 55990</p>
  </div>

  <ul class="contacts">
    <li>
      <svg viewBox="0 0 16 16"><rect x="4" y="1" width="8" height="14" rx="1.5" fill="none" stroke="var(--brand-red)" stroke-width="1.6"/><circle cx="8" cy="12.5" r="0.9" fill="var(--brand-red)"/></svg>
      612-555-0147
    </li>
    <li>
      <svg viewBox="0 0 16 16"><rect x="1" y="3" width="14" height="10" fill="none" stroke="var(--brand-red)" stroke-width="1.6"/><path d="M1 3 L8 9 L15 3" fill="none" stroke="var(--brand-red)" stroke-width="1.6"/></svg>
      cobaltfinishworksmn@mailbox.example
    </li>
    <li>
      <svg viewBox="0 0 16 16"><circle cx="8" cy="8" r="6.5" fill="none" stroke="var(--brand-red)" stroke-width="1.6"/><ellipse cx="8" cy="8" rx="2.8" ry="6.5" fill="none" stroke="var(--brand-red)" stroke-width="1.2"/><path d="M1.5 8 H14.5" stroke="var(--brand-red)" stroke-width="1.2"/></svg>
      www.cobaltfinishworks.example
    </li>
  </ul>
</section>

<section class="card card--back" aria-label="Business card back">
  <div class="back-frame">
    <div class="back-panel">
      <article class="service">
        <div class="service__photo service__photo--basement" role="img" aria-label="Photo of a finished basement with bar and media wall"></div>
        <h3 class="service__title">Basement Finish</h3>
        <p class="service__text">We strive to meet or exceed your expectations. We know the importance of deadlines, and you can depend on Cobalt Finish Works to get your home improvement job done on time and on budget.</p>
      </article>
      <article class="service">
        <div class="service__photo service__photo--kitchen" role="img" aria-label="Photo of a remodeled kitchen with island and pendant lights"></div>
        <h3 class="service__title">Kitchen Remodeling</h3>
        <p class="service__text">With 20 Years of experience, Cobalt Finish Works has the knowledge and ability to handle your home improvement project, no matter how big or small.</p>
      </article>
      <article class="service">
        <div class="service__photo service__photo--install" role="img" aria-label="Photo of a stone feature wall with mounted TV and fireplace"></div>
        <h3 class="service__title">Flatpack Installations</h3>
        <p class="service__text">What we do isn't just a job; it's our passion. We have dedicated ourselves to making sure we do the best job possible because we want the best for you.</p>
      </article>
    </div>
  </div>
</section>

</body>
</html>
```